2018 Fundraiser Event Flier

We are a non profit that works in the homeless community, The Lanternbrook Alliance. We offer a unique program of supported employment that is all about community engagement and building relationships not only with our participants but with community businesses and non profit partners. Our mission statement is "We seek and foster partnerships between the business and nonprofit communities to respectfully and effectively guide individuals from disenfranchised communities forward in sustainable employment to realize their potential of fully enriched lives for themselves and their families" We are having a fundraising event on Dec 13 and need a flier to advertise the event both via email and physical postings. We like a black background and bright colors (see uploaded example) and want to advertise the event and a small amount about who we are. Fun and bright. We will upload two of our logos and two photos that we have used in branding previously.

```html
<!DOCTYPE html>
<html lang="en">
<head>
<meta charset="utf-8">
<title>Lanternbrook Alliance Fundraiser Flier</title>
<link href="https://fonts.googleapis.com/css2?family=Fredoka:wght@400&family=Lato:wght@400;700&family=Lobster&family=Raleway:wght@700&display=swap" rel="stylesheet">
<style>
  :root {
    --page: #e8e8e8;
    --paper-top: #ffffff;
    --paper-bottom: #ececec;
    --ink: #1f1f1f;
    --gold: #f4b81c;
    --green: #76bc3f;
    --blue: #2f8ccb;
    --band: #3a87c4;
    --plum: #a1449a;
    --photo-light: #9a9a9a;
    --photo-dark: #3c3c3c;
  }
  * { margin: 0; padding: 0; box-sizing: border-box; }
  html, body { width: 1200px; height: 918px; overflow: hidden; background: var(--page); }
  .flier {
    position: absolute; left: 297px; top: 29px; width: 606px; height: 860px;
    background: linear-gradient(180deg, var(--paper-top) 40%, var(--paper-bottom));
    overflow: hidden; box-shadow: 0 4px 14px rgba(0,0,0,.12);
    font-family: "Lato", sans-serif; color: var(--ink);
  }
  .hero-photo {
    position: absolute; left: 0; top: 0; width: 606px; height: 340px;
    background: linear-gradient(160deg, var(--photo-light), var(--photo-dark) 60%, #6a6a6a);
  }
  .torn-edge { position: absolute; left: 0; top: 300px; }
  .brand-notch { position: absolute; left: 0; top: 0; }
  .brand-name {
    position: absolute; left: 228px; top: 58px; width: 150px; text-align: center;
    font-family: "Lato", sans-serif; font-weight: 700; font-size: 11px; line-height: 1.25;
    color: var(--ink); text-transform: uppercase; letter-spacing: .5px;
  }
  .headline {
    position: absolute; left: 58px; top: 440px; width: 492px; text-align: center;
    font-family: "Fredoka", sans-serif; font-size: 30px; color: var(--gold);
    letter-spacing: .5px; white-space: nowrap;
  }
  .intro {
    position: absolute; left: 52px; top: 484px; width: 498px;
    font-size: 11.6px; line-height: 15px;
  }
  .partners { position: absolute; left: 52px; top: 530px; width: 498px; text-align: center; font-size: 11.6px; line-height: 15px; }
  .pitch { position: absolute; text-align: right; }
  .pitch .verb { display: block; font-size: 27px; line-height: 26px; font-family: "Lato", sans-serif; }
  .pitch .detail { display: block; font-family: "Lobster", cursive; font-size: 19px; line-height: 20px; color: var(--ink); }
  .pitch-enjoy { left: 107px; top: 566px; } .pitch-enjoy .verb { color: var(--green); }
  .pitch-discover { left: 220px; top: 600px; } .pitch-discover .verb { color: var(--gold); }
  .pitch-support { left: 357px; top: 634px; } .pitch-support .verb { color: var(--blue); }
  .event-date { position: absolute; left: 29px; top: 668px; font-size: 24px; font-weight: 700; color: var(--green); }
  .event-venue { position: absolute; left: 29px; top: 697px; font-size: 13.5px; font-weight: 700; color: var(--plum); line-height: 17px; text-transform: uppercase; }
  .mission-band {
    position: absolute; left: 0; top: 749px; width: 606px; height: 111px; background: var(--band);
    padding: 18px 19px 0; color: #fff; font-family: "Raleway", sans-serif; font-size: 11px;
    line-height: 15px; text-transform: uppercase; text-align: justify; letter-spacing: .2px;
  }
</style>
</head>
<body>
<main class="flier">
  <div class="hero-photo" role="img" aria-label="Black and white photo of a man in a knit cap holding a cardboard sign asking for work"></div>
  <svg class="torn-edge" width="606" height="140" viewBox="0 0 606 140" aria-hidden="true">
    <path d="M0 22 L30 18 L52 28 L70 30 L95 44 L120 70 L150 82 L185 86 L205 70 L220 40 L245 30 L270 26 L300 22 L330 18 L360 20 L390 14 L420 18 L450 12 L480 16 L510 10 L540 14 L570 8 L606 12 L606 140 L0 140 Z" fill="#fafafa"/>
    <path d="M95 44 L120 70 L150 82 L185 86 L205 70" fill="none" stroke="#d0d0d0" stroke-width="2"/>
  </svg>
  <svg class="brand-notch" width="606" height="140" viewBox="0 0 606 140" aria-hidden="true">
    <polygon points="164,0 441,0 303,138" fill="#ffffff"/>
  </svg>
  <div class="brand-name">The Lanternbrook Alliance</div>

  <h1 class="headline">JOIN US ON OUR FUNDRAISER</h1>
  <p class="intro">Help us provide support through the placement of Peer Mentor/Trainers in the workforce creating a safe and dynamic training workspace within the business operations of our Community Partners:</p>
  <p class="partners">- Summit Staffing Partners / Highline Wildlife Park<br>- Harborview Grand Hotel / Aspen Row</p>

  <div class="pitch pitch-enjoy"><span class="verb">ENJOY.</span><span class="detail">great beer</span></div>
  <div class="pitch pitch-discover"><span class="verb">DISCOVER.</span><span class="detail">new friends</span></div>
  <div class="pitch pitch-support"><span class="verb">SUPPORT.</span><span class="detail">your community</span></div>

  <div class="event-date">DECEMBER 13TH</div>
  <div class="event-venue">Copperleaf Brewing Co<br>148 Meridian Ave Riverton CO 80477</div>

  <p class="mission-band">We seek and foster partnerships between the business and nonprofit communities to respectfully and effectively guide individuals from disenfranchised communities forward in sustainable employment to realize their potential of fully enriched lives for themselves and their families</p>
</main>
</body>
</html>
```